Plakate für Haushaltsnahe Dienstleistungen sowie Alltagsbegleitung
Zielgruppe
Wir sind eine Firma die Haushaltsnahe Dienstleistungen sowie Alltagsbegleitung anbietet. Unser Hauptkundenklientel sind Pflegebedürftige Menschen denen Haushaltshilfe von der Pflegekasse zu steht.
Aufgabenstellung
Es soll ein Roll-Up werden. Es soll drauf stehen: Abrechnung mit allen Pflegekasse möglich über den Entlastungsbetrag (ab Pflegegrad 1 bis 5) sowie Verhinderungspflege. Kontaktdaten sowie unsere Vorteile sollen auch drauf stehen.

```html
<!DOCTYPE html>
<html lang="de">
<head>
<meta charset="utf-8">
<title>Roll-Up Lindhof Haushaltshilfen</title>
<link rel="stylesheet" href="https://fonts.googleapis.com/css2?family=Fira+Sans:wght@400;500;600;700&display=swap">
<style>
  :root {
    --red: #c8203a;
    --red-light: #d42e3f;
    --red-deep: #bd1d37;
    --berry: #b52a55;
    --ink: #3a3a3a;
    --badge: #4a4647;
    --white: #ffffff;
    --paper: #f7f7f7;
    --stage: #c8c8c8;
    --soft-line: #e6e2e3;
  }
  * { box-sizing: border-box; margin: 0; padding: 0; }
  html, body { width: 1200px; height: 1200px; overflow: hidden; }
  body {
    background: var(--stage);
    font-family: "Fira Sans", Arial, sans-serif;
    position: relative;
  }
  .rollup {
    position: absolute;
    left: 360px; top: 24px;
    width: 480px; height: 1152px;
    background: var(--white);
    overflow: hidden;
  }
  .rollup__shapes { position: absolute; inset: 0; }
  .brand {
    position: absolute; left: 56px; top: 30px;
    display: flex; align-items: center; gap: 16px;
  }
  .brand__dot {
    width: 78px; height: 78px; border-radius: 50%;
    border: 6px solid var(--red);
  }
  .brand__name {
    color: var(--ink); font-weight: 600;
    font-size: 44px; line-height: 1; letter-spacing: 1px;
  }
  .brand__name small {
    display: block; font-size: 15.5px; letter-spacing: 1px; margin-top: 6px;
  }
  .badge {
    position: absolute; left: 334px; top: 102px;
    width: 108px; height: 108px; border-radius: 50%;
    background: var(--badge); border: 3px solid var(--white);
    color: var(--white); font-weight: 600; font-size: 14px; line-height: 1.15;
    display: flex; align-items: center; justify-content: center; text-align: center;
  }
  .headline {
    position: absolute; left: 0; right: 0; top: 222px;
    text-align: center; color: var(--white);
    font-weight: 700; font-size: 33px; line-height: 46px; letter-spacing: 3px;
  }
  .intro {
    position: absolute; left: 36px; right: 36px; top: 338px;
    text-align: center; color: var(--white);
    font-size: 9px; line-height: 13.5px; letter-spacing: 0.6px;
  }
  .section-pill {
    position: absolute; left: 54px; top: 440px;
    width: 368px; height: 44px; border-radius: 22px;
    background: var(--red); border: 2px solid var(--white);
    box-shadow: 0 3px 4px rgba(0,0,0,0.18);
    color: var(--white); font-weight: 700; font-size: 31px; letter-spacing: 3px;
    display: flex; align-items: center; justify-content: center;
  }
  .benefit {
    position: absolute; width: 200px; text-align: center;
  }
  .benefit__icon { width: 144px; height: 144px; display: block; margin: 0 auto; }
  .benefit__label {
    margin-top: 10px; color: var(--ink); font-weight: 600;
    font-size: 13px; line-height: 18px; letter-spacing: 1px;
  }
  .benefit--a { left: 26px; top: 528px; }
  .benefit--b { left: 242px; top: 528px; width: 220px; }
  .benefit--c { left: 26px; top: 772px; }
  .benefit--d { left: 252px; top: 776px; }
  .footer-company {
    position: absolute; left: 36px; top: 1038px;
    color: var(--white); font-size: 13.5px; line-height: 19px; letter-spacing: 1.2px;
  }
  .footer-company strong { display: block; font-weight: 600; letter-spacing: 1.5px; }
  .footer-company p { margin-top: 6px; }
  .footer-contact {
    position: absolute; right: 36px; top: 1050px;
    text-align: right; color: var(--white);
    font-size: 13.5px; line-height: 19px; letter-spacing: 1.2px;
  }
  .footer-contact strong { display: block; font-weight: 600; letter-spacing: 1.5px; margin-bottom: 6px; }
</style>
</head>
<body>
<main class="rollup">
  <svg class="rollup__shapes" width="480" height="1152" viewBox="0 0 480 1152" aria-hidden="true">
    <defs>
      <linearGradient id="redField" x1="0" y1="0" x2="1" y2="1">
        <stop offset="0" stop-color="var(--red-light)"/>
        <stop offset="1" stop-color="var(--red-deep)"/>
      </linearGradient>
      <linearGradient id="berryBand" x1="0" y1="0" x2="1" y2="0">
        <stop offset="0" stop-color="var(--red-light)"/>
        <stop offset="1" stop-color="var(--berry)"/>
      </linearGradient>
      <linearGradient id="paperFade" x1="0" y1="0" x2="0" y2="1">
        <stop offset="0" stop-color="var(--white)"/>
        <stop offset="1" stop-color="var(--paper)"/>
      </linearGradient>
    </defs>
    <rect width="480" height="1152" fill="url(#paperFade)"/>
    <path class="field-top" d="M0 114 C150 170 330 178 480 140 L480 482 C330 478 150 472 0 436 Z" fill="url(#redField)"/>
    <path class="field-top-band" d="M0 124 C150 180 330 188 480 150 L480 178 C330 214 150 210 0 150 Z" fill="url(#berryBand)" opacity="0.55"/>
    <path class="divider-line" d="M0 436 C150 472 330 478 480 482 L480 494 C330 490 150 484 0 446 Z" fill="var(--soft-line)"/>
    <path class="field-bottom-line" d="M0 946 C150 984 330 1012 480 1018 L480 1030 C330 1022 150 994 0 958 Z" fill="var(--soft-line)"/>
    <path class="field-bottom" d="M0 958 C150 994 330 1022 480 1030 L480 1152 L0 1152 Z" fill="url(#redField)"/>
  </svg>

  <div class="brand">
    <span class="brand__dot"></span>
    <div class="brand__name">LINDHOF<small>HAUSHALTSHILFEN &amp; MEHR</small></div>
  </div>

  <div class="badge">Jetzt Termin<br>vereinbaren!</div>

  <h1 class="headline">BENÖTIGEN SIE<br>HILFE IM HAUSHALT?</h1>

  <p class="intro">Wir bieten Haushaltshilfen und Alltagsbegleiter für Privathaushalte an. Unsere Hauptkundenklientel sind Pflegebedürftige Menschen denen eine Haushaltshilfe von der Pflegekasse zusteht. Weitere Kunden sind Familien und/oder Singlehaushalte, die eine Haushaltshilfe benötigen.</p>

  <div class="section-pill">UNSERE VORTEILE</div>

  <section class="benefit benefit--a">
    <svg class="benefit__icon" viewBox="0 0 144 144" aria-hidden="true">
      <circle cx="72" cy="72" r="66" fill="none" stroke="var(--red)" stroke-width="5"/>
      <path d="M46 30 H86 L104 48 V108 a6 6 0 0 1 -6 6 H46 a6 6 0 0 1 -6 -6 V36 a6 6 0 0 1 6 -6 Z" fill="var(--red)"/>
      <path d="M86 30 V48 H104" fill="var(--white)" opacity="0.9"/>
      <rect x="48" y="44" width="12" height="5" rx="2.5" fill="var(--white)"/>
      <rect x="48" y="56" width="12" height="5" rx="2.5" fill="var(--white)"/>
      <text x="72" y="102" text-anchor="middle" font-family="Fira Sans, sans-serif" font-weight="700" font-size="40" fill="var(--white)">$</text>
    </svg>
    <p class="benefit__label">ABRECHNUNG MIT ALLEN<br>PFLEGEKASSEN MÖGLICH</p>
  </section>

  <section class="benefit benefit--b">
    <svg class="benefit__icon" viewBox="0 0 144 144" aria-hidden="true">
      <circle cx="72" cy="72" r="66" fill="none" stroke="var(--red)" stroke-width="5"/>
      <path d="M64 24 h14 v14 h14 v14 h-14 v14 h-14 v-14 h-14 v-14 h14 Z" fill="var(--red)" stroke="var(--red)" stroke-width="2" stroke-linejoin="round"/>
      <path d="M30 90 h18 c8 0 14 -6 24 -6 h12 a5 5 0 0 1 0 10 h-16 h18 l22 -14 a6 6 0 0 1 8 9 l-24 18 c-6 4 -12 5 -18 5 h-44 Z" fill="var(--red)"/>
    </svg>
    <p class="benefit__label">ABRECHNUNG ÜBER DEN<br>ENTLASTUNGSBETRAG VON<br>MIND. 125 € MTL. AB<br>PFLEGEGRAD 1 MÖGLICH</p>
  </section>

  <section class="benefit benefit--c">
    <svg class="benefit__icon" viewBox="0 0 144 144" aria-hidden="true">
      <circle cx="72" cy="72" r="66" fill="none" stroke="var(--red)" stroke-width="5"/>
      <path d="M77 66 L58 48 a11 11 0 0 1 19 -12 a11 11 0 0 1 19 12 Z" fill="var(--red)"/>
      <path d="M30 90 h18 c8 0 14 -6 24 -6 h12 a5 5 0 0 1 0 10 h-16 h18 l22 -14 a6 6 0 0 1 8 9 l-24 18 c-6 4 -12 5 -18 5 h-44 Z" fill="var(--red)"/>
    </svg>
    <p class="benefit__label">AUCH ÜBER DIE<br>VERHINDERUNGSPFLEGE</p>
  </section>

  <section class="benefit benefit--d">
    <svg class="benefit__icon" viewBox="0 0 144 144" aria-hidden="true">
      <circle cx="72" cy="72" r="66" fill="none" stroke="var(--red)" stroke-width="5"/>
      <path d="M38 28 H76 L94 46 V110 a6 6 0 0 1 -6 6 H38 a6 6 0 0 1 -6 -6 V34 a6 6 0 0 1 6 -6 Z" fill="var(--red)"/>
      <path d="M76 28 V46 H94" fill="var(--white)" opacity="0.9"/>
      <path d="M42 96 c4 -10 6 -10 8 0 c2 6 4 -8 7 -4 c3 4 4 6 10 4" fill="none" stroke="var(--white)" stroke-width="3" stroke-linecap="round"/>
      <path d="M72 96 L108 60 l10 10 L82 106 l-14 4 Z" fill="var(--red)" stroke="var(--white)" stroke-width="4" stroke-linejoin="round"/>
    </svg>
    <p class="benefit__label">HILFE BEI DER<br>ANTRAGSSTELLUNG</p>
  </section>

  <address class="footer-company" style="font-style:normal">
    <strong>LINDHOF<br>HAUSHALTSHILFEN &amp; MEHR</strong>
    <p>Mühlgasse 14<br>70100 Stadtfeld</p>
  </address>

  <address class="footer-contact" style="font-style:normal">
    <strong>KONTAKT</strong>
    0700 12345678<br>
    info@lindhof-hilfe.de<br>
    www.lindhof-hilfe.de
  </address>
</main>
</body>
</html>
```